Web Page needed for Dr. Wanbrook Consult

The company works in the consultant business for processes in large projects our of engineering and construction business. We develop strategies but work also in critical projects to get them right.
The page should have a modern appearance but though a classy and luxury touch.
Updates

The project was bought in a package, logo plus web page. Now the designers do submit logos again, although the logo has been set. This part is only the web site. I changed the text to clarify it, I contacted support to put that right, but that needs an extension of minimum 7 days to catch up.

Due to the confusion in the project, it was first set up as logo project and later corrected (I have no clue how that happened, as I bought a package with logo + web, and logo is already done), there is a large delay in getting feedback. Please be so kind and extend until 31.01. In Europe there is holidays until 07.01. and I have no time to discuss the topics with my client until 10.01., than we need to feed in response and get changes done.

Logo Text

The logo is already fixed, I asked for web page.

Number of Pages Required

5+ page

Font styles to use
Sans Serif

Colors

Designer to choose colors to be used in the design.

Requirements
Must have
• Home/Start
• Lean Construction
• Lean Equipment
• Lean Design
• Lean Training
• Team
• Contact
• Imprint
Nice to have
• Darker color, luxury appearance, please integrate the logo in the attachment here.
• I would like to have a web page with animated context, such as this one here: https://tovalmerworks.example

```html
<!DOCTYPE html>
<html lang="en">
<head>
<meta charset="utf-8">
<title>Dr. Wanbrook Consult</title>
<link rel="stylesheet" href="https://fonts.googleapis.com/css2?family=Rajdhani:wght@500;600;700&family=Rubik:wght@400;500&display=swap">
<style>
:root{
  --accent:#a3e300;
  --ink:#2b2b2b;
  --text:#444;
  --muted:#9a9a9a;
  --band:#f4f4f4;
  --line:#dcdcdc;
  --footer:#0f5aa6;
  --footer-dark:#0b4886;
  --white:#fff;
}
*{box-sizing:border-box;margin:0;padding:0}
html,body{width:1200px;height:3532px;overflow:hidden}
body{position:relative;background:var(--white);font-family:'Rubik',sans-serif;color:var(--text)}
.abs{position:absolute}
.heading{font-family:'Rajdhani',sans-serif;font-weight:700;text-transform:uppercase;color:var(--ink);letter-spacing:.3px}
.photo{position:absolute}

/* hero */
.hero{position:absolute;left:0;top:0;width:1200px;height:466px;background:linear-gradient(180deg,rgba(40,34,28,.55),rgba(40,34,28,.45)),linear-gradient(100deg,#6b5a47 0%,#8b7b62 30%,#b49a58 48%,#7a6a55 70%,#a07050 90%,#5f5040 100%)}
.brand{position:absolute;display:flex;align-items:center;gap:10px;font-family:'Rubik',sans-serif;font-weight:500;color:var(--white)}
.brand-mark{width:26px;height:26px;border:2px solid var(--white)}
.nav{position:absolute;top:59px;left:500px;display:flex;gap:19px;font-family:'Rubik',sans-serif;font-size:11px;font-weight:500;color:var(--white);text-transform:uppercase;letter-spacing:.4px}
.nav-imprint{position:absolute;left:1064px;top:45px;width:70px;height:43px;border:2px solid var(--accent);color:var(--accent);font-size:11px;font-weight:500;display:flex;align-items:center;justify-content:center;text-transform:uppercase}
.hero-title{position:absolute;top:205px;width:1200px;text-align:center;font-size:42px;color:var(--white)}
.hero-sub{position:absolute;top:284px;width:1200px;text-align:center;font-size:13px;color:var(--white)}
.watch{position:absolute;left:509px;top:353px;font-family:'Rajdhani',sans-serif;font-weight:700;font-size:16px;color:var(--accent)}
.play{position:absolute;left:613px;top:325px}

/* services */
.services{position:absolute;left:0;top:466px;width:1200px;height:202px;background:var(--band)}
.service{position:absolute;top:77px;display:flex}
.service-icon{width:30px;height:30px;margin-top:7px}
.service-rule{width:1px;height:54px;background:var(--line);margin:0 14px 0 12px}
.service h3{font-family:'Rubik',sans-serif;font-weight:500;font-size:17px;color:#444;margin-top:1px}
.service p{font-size:11px;color:var(--muted);margin-top:9px}

/* feature rows */
.section-title{position:absolute;font-size:27px}
.lead{position:absolute;font-size:14px;line-height:26px;color:var(--text)}
.ticks{position:absolute;list-style:none;font-size:11.5px;color:var(--muted)}
.ticks li{height:24.5px;padding-left:26px;position:relative}
.ticks li::before{content:"+";position:absolute;left:0;top:-3px;color:var(--accent);font-size:15px}
.btn{position:absolute;background:var(--accent);color:var(--ink);font-family:'Rajdhani',sans-serif;font-weight:600;font-size:13px;text-transform:uppercase;display:flex;align-items:center;justify-content:center}
.corner{position:absolute;width:46px;height:46px;border-color:var(--accent);border-style:solid;border-width:0}
.corner.tl{border-top-width:2px;border-left-width:2px}
.corner.br{border-bottom-width:2px;border-right-width:2px}

/* stats band */
.together{position:absolute;left:0;top:1514px;width:1200px;height:447px;background:radial-gradient(ellipse 260px 200px at 860px 300px,rgba(214,160,20,.85),transparent 70%),linear-gradient(90deg,#2a2a25 0%,#34332c 40%,#37424f 60%,#3b5877 80%,#6a6f72 100%)}
.band-title{position:absolute;font-size:27px;color:var(--accent)}
.band-text{position:absolute;font-size:13.5px;line-height:27px;color:var(--white)}
.stat-num{position:absolute;font-family:'Rajdhani',sans-serif;font-weight:700;font-size:24px;color:var(--accent)}
.stat-label{position:absolute;font-size:11px;color:var(--white);text-transform:uppercase}
.ghost-btn{position:absolute;border:2px solid var(--white);color:var(--white);font-family:'Rajdhani',sans-serif;font-weight:700;font-size:15px;text-transform:uppercase;display:flex;align-items:center;justify-content:center}

/* values */
.believe{position:absolute;top:2036px;width:1200px;text-align:center;font-size:26px;line-height:32px}
.card{position:absolute;top:2164px;width:318px;height:169px;border:2px solid var(--line)}
.card h4{position:absolute;left:92px;top:28px;font-family:'Rajdhani',sans-serif;font-weight:700;font-size:18px;color:var(--ink)}
.card p{position:absolute;left:92px;top:68px;font-size:12.5px;line-height:26px;color:var(--text);width:180px}
.card svg{position:absolute;left:28px;top:56px}
.dream{position:absolute;left:66px;top:2398px;font-size:27px;line-height:31px}
.dream-text{position:absolute;left:440px;top:2398px;width:700px;font-size:13.5px;line-height:26px;color:var(--text)}

/* partners */
.partners{position:absolute;left:0;top:2554px;width:1200px;height:238px;background:var(--band)}
.partner{position:absolute;top:83px;display:flex;align-items:center;gap:10px;font-family:'Rubik',sans-serif;font-weight:500;font-size:18px;color:#666}
.partner span.sq{width:30px;height:30px;background:#6a6a6a;display:block}
.dots{position:absolute;left:546px;top:160px;display:flex;gap:12px}
.dots i{width:18px;height:3px;background:#c9c9c9;display:block}
.dots i.on{background:var(--accent)}

/* cta */
.cta{position:absolute;left:0;top:2792px;width:1200px;height:428px;background:radial-gradient(ellipse 300px 200px at 300px 190px,rgba(200,155,25,.9),transparent 70%),linear-gradient(90deg,#5a4a2a 0%,#4a4030 40%,#3a3630 60%,#2e2b27 100%)}
.cta-feature{position:absolute;color:var(--white)}
.cta-feature h5{font-family:'Rubik',sans-serif;font-weight:500;font-size:16.5px;line-height:23px}
.cta-feature p{font-size:11px;line-height:22px;margin-top:3px}
.vline{position:absolute;width:2px;height:70px;background:var(--accent)}

/* footer */
.footer{position:absolute;left:0;top:3220px;width:1200px;height:271px;background:var(--footer);color:var(--white)}
.footer h6{position:absolute;top:52px;font-family:'Rajdhani',sans-serif;font-weight:500;font-size:20px;text-transform:uppercase}
.footer-about{position:absolute;left:66px;top:116px;width:320px;font-size:11px;line-height:22px}
.social{position:absolute;top:176px;width:40px;height:40px;border:1px solid rgba(255,255,255,.45);border-radius:50%}
.contact{position:absolute;left:446px;top:102px;list-style:none;font-size:11px;line-height:24.5px}
.contact li::before{content:"•";margin-right:8px}
.resources{position:absolute;left:816px;top:97px;list-style:none;font-size:14px;line-height:25px;text-transform:uppercase;border-left:1px solid rgba(255,255,255,.5)}
.resources li{position:relative;padding-left:29px}
.resources li::before{content:"";position:absolute;left:0;top:12px;width:20px;height:1px;background:rgba(255,255,255,.5)}
.copyright{position:absolute;left:0;top:3491px;width:1200px;height:41px;background:var(--footer-dark);color:var(--white);font-size:11px;display:flex;align-items:center;justify-content:center}
</style>
</head>
<body>

<header class="hero" role="img" aria-label="Photo of three engineers in hard hats and safety vests reviewing plans on a construction site">
</header>
<div class="brand" style="left:71px;top:48px;font-size:21px"><span class="brand-mark"></span>Dr. Wanbrook Consult</div>
<nav class="nav">
  <span>Home</span><span>Lean Construction</span><span>Lean Equipment</span><span>Lean Design</span><span>Lean Training</span>
</nav>
<div class="nav-imprint">Imprint</div>
<h1 class="heading hero-title" style="color:var(--white)">The best constructions company since 1895</h1>
<p class="hero-sub">Each of us is carving a stone, erecting a column, or cutting a piece of stained glass in the construction of something much bigger than ourselves.</p>
<div class="watch">WATCH VIDEO</div>
<svg class="play" width="76" height="76" viewBox="0 0 76 76"><circle cx="38" cy="38" r="38" fill="rgba(255,255,255,.18)"/><path d="M28 22 L54 38 L28 54 Z" fill="#fff"/></svg>

<section class="services">
  <div class="service" style="left:66px">
    <svg class="service-icon" viewBox="0 0 30 30"><rect x="1" y="1" width="28" height="28" fill="none" stroke="#555" stroke-width="1.5"/><path d="M7 23h16M10 23l4-9 5 4" fill="none" stroke="#555" stroke-width="2"/><circle cx="16" cy="9" r="2.5" fill="#555"/></svg>
    <span class="service-rule"></span>
    <div><h3>Construction</h3><p>Speed, flexibility</p></div>
  </div>
  <div class="service" style="left:347px">
    <svg class="service-icon" viewBox="0 0 30 30"><rect x="1" y="1" width="28" height="28" fill="none" stroke="#555" stroke-width="1.5"/><path d="M8 8l14 14M22 8L8 22" stroke="#555" stroke-width="2.5"/></svg>
    <span class="service-rule"></span>
    <div><h3>Equipment</h3><p>Speed, flexibility</p></div>
  </div>
  <div class="service" style="left:628px">
    <svg class="service-icon" viewBox="0 0 30 30"><rect x="1" y="1" width="28" height="28" fill="none" stroke="#555" stroke-width="1.5"/><path d="M6 22h18M8 22v-6h14v6M11 16l4-6 4 6" fill="none" stroke="#555" stroke-width="2"/></svg>
    <span class="service-rule"></span>
    <div><h3>Design</h3><p>Complex customer works</p></div>
  </div>
  <div class="service" style="left:909px">
    <svg class="service-icon" viewBox="0 0 30 30"><rect x="1" y="1" width="28" height="28" fill="none" stroke="#555" stroke-width="1.5"/><path d="M9 12h12M11 12a4 4 0 0 1 8 0M10 24v-4a5 5 0 0 1 10 0v4" fill="none" stroke="#555" stroke-width="2"/><circle cx="15" cy="16" r="2.5" fill="#555"/></svg>
    <span class="service-rule"></span>
    <div><h3>Training</h3><p>Complex customer works</p></div>
  </div>
</section>

<h2 class="heading section-title" style="left:66px;top:740px">Sustainability goals</h2>
<p class="lead" style="left:66px;top:800px;width:520px">Our team of experts in the areas of architecture, engineering, management and construction bring you the insight and advice you need for your project.</p>
<ul class="ticks" style="left:66px;top:886px">
  <li>Ecoligic materials and oils</li>
  <li>Human charity for thirt world countries</li>
  <li>Renovable products from the scratch</li>
</ul>
<div class="btn" style="left:66px;top:1001px;width:205px;height:41px">About our sustainability</div>
<span class="corner tl" style="left:618px;top:734px"></span>
<span class="corner br" style="left:1098px;top:996px"></span>
<div class="photo" style="left:628px;top:742px;width:506px;height:292px;background:linear-gradient(160deg,#c9ced3 0%,#8d949a 40%,#6e6a62 70%,#a07b55 100%)" role="img" aria-label="Photo of a modern glass and steel atrium interior with a staircase"></div>

<span class="corner tl" style="left:56px;top:1127px"></span>
<span class="corner br" style="left:535px;top:1393px"></span>
<div class="photo" style="left:66px;top:1137px;width:506px;height:292px;background:linear-gradient(120deg,#b08a5a 0%,#d2b48a 35%,#8a7255 65%,#c9a26b 100%)" role="img" aria-label="Photo of a builder and a colleague studying plans on a timber-frame site"></div>
<h2 class="heading section-title" style="left:628px;top:1136px">Certified</h2>
<p class="lead" style="left:628px;top:1195px;width:500px">Lorem ipsum dolor sit amet consectetur adipiscing elitsede.</p>
<ul class="ticks" style="left:628px;top:1255px">
  <li>Day to day checks</li>
  <li>Humans quality operators</li>
  <li>ISO-2002 annual certifications</li>
</ul>
<div class="btn" style="left:628px;top:1370px;width:193px;height:41px">Get more informations</div>

<section class="together" role="img" aria-label="Photo of a worker holding a yellow hard hat and rolled plans"></section>
<h2 class="heading band-title" style="left:66px;top:1587px">Let build together</h2>
<p class="band-text" style="left:66px;top:1646px;width:500px">Laboris nisi ut aliquip ex ea commodo consequat. Duis aute irure dolor in reprehenderit in voluptate velit esse cillum dolore eu fugiat nulla pariatur.</p>
<svg class="abs" style="left:71px;top:1777px" width="24" height="26" viewBox="0 0 24 26"><rect x="1" y="1" width="22" height="24" fill="none" stroke="#a3e300" stroke-width="2"/><circle cx="12" cy="10" r="3.5" fill="#a3e300"/><path d="M5 21h14l-3-6H8z" fill="#a3e300"/></svg>
<svg class="abs" style="left:352px;top:1777px" width="24" height="26" viewBox="0 0 24 26"><rect x="1" y="1" width="22" height="24" fill="none" stroke="#a3e300" stroke-width="2"/><circle cx="8" cy="9" r="2.5" fill="#a3e300"/><circle cx="16" cy="9" r="2.5" fill="#a3e300"/><path d="M5 20v-6h6v6M13 20v-6h6v6" fill="#a3e300"/></svg>
<div class="stat-num" style="left:66px;top:1827px">850.034</div>
<div class="stat-label" style="left:66px;top:1867px">Square meters built</div>
<div class="stat-num" style="left:347px;top:1827px">125.000</div>
<div class="stat-label" style="left:347px;top:1867px">Worked with us</div>
<div class="ghost-btn" style="left:791px;top:1711px;width:181px;height:52px">Join our team</div>

<h2 class="heading believe">We believe in making it easier for organisations to<br>work and grow on an international scale</h2>
<div class="card" style="left:66px">
  <svg width="28" height="30" viewBox="0 0 28 30"><rect x="1" y="1" width="26" height="28" fill="none" stroke="#a3e300" stroke-width="2"/><circle cx="9" cy="10" r="3" fill="#a3e300"/><circle cx="19" cy="10" r="3" fill="#a3e300"/><path d="M5 24v-8h8v8M15 24v-8h8v8" fill="#a3e300"/></svg>
  <h4>LEADERSHIP</h4>
  <p>Purus expedita fusce temporibus est odit mi quoeliquid sempere</p>
</div>
<div class="card" style="left:440px">
  <svg width="28" height="30" viewBox="0 0 28 30"><rect x="1" y="1" width="26" height="28" fill="none" stroke="#a3e300" stroke-width="2"/><path d="M5 15q9-9 18 0q-9 9-18 0z" fill="none" stroke="#a3e300" stroke-width="2"/><circle cx="14" cy="15" r="3" fill="#a3e300"/></svg>
  <h4>VISION</h4>
  <p>Purus expedita fusce temporibus est odit mi quoeliquid sempere</p>
</div>
<div class="card" style="left:816px">
  <svg width="28" height="30" viewBox="0 0 28 30"><rect x="1" y="1" width="26" height="28" fill="none" stroke="#a3e300" stroke-width="2"/><path d="M14 23l-7-7a4 4 0 0 1 7-5a4 4 0 0 1 7 5z" fill="#a3e300"/></svg>
  <h4>CORE VALUES</h4>
  <p>Purus expedita fusce temporibus est odit mi quoeliquid sempere</p>
</div>

<h2 class="heading dream">Build your dream<br>home now!</h2>
<p class="dream-text">Lorem ipsum dolor sit amet consectetur adipiscing elitsed do eiusmod tempor incididunt utlabore et dolore magna aliqua. Utenim ad minim veniam quis nostrud exercitation ullamco laboris nisi ut aliquip ex ea commodo consequat. Duis aute irure dolor in reprehenderit in voluptate velit esse cillum dolore.</p>

<section class="partners">
  <div class="partner" style="left:100px"><span class="sq"></span>ARKLINE</div>
  <div class="partner" style="left:320px"><span class="sq"></span>LINEFORM</div>
  <div class="partner" style="left:516px"><span class="sq"></span>NORTHLAB</div>
  <div class="partner" style="left:766px"><span class="sq"></span>BLOCKWORKS</div>
  <div class="partner" style="left:968px"><span class="sq"></span>GRIDMAKE</div>
  <div class="dots"><i></i><i class="on"></i><i></i><i></i></div>
</section>

<section class="cta" role="img" aria-label="Photo of a yellow hard hat and work gloves on a table"></section>
<h2 class="heading band-title" style="left:628px;top:2865px">Let build something together</h2>
<p class="band-text" style="left:628px;top:2925px;width:520px">Laboris nisi ut aliquip ex ea commodo consequat. Duis aute irure dolor in reprehenderit in voluptate velit esse cillum dolore eu fugiat nulla pariatur. Arte utlabrure dolor iore et dolore muralla pertino caro aliqua.</p>
<div class="ghost-btn" style="left:252px;top:2980px;width:133px;height:52px">Imprint</div>
<svg class="abs" style="left:633px;top:3080px" width="24" height="28" viewBox="0 0 24 28"><rect x="1" y="1" width="22" height="26" fill="none" stroke="#a3e300" stroke-width="2"/><path d="M6 21a6 6 0 0 1 12 0zM9 13h6l-1-5h-4z" fill="#a3e300"/></svg>
<span class="vline" style="left:701px;top:3072px"></span>
<div class="cta-feature" style="left:717px;top:3071px"><h5>Free quote</h5><p>Lorem ipsum doler<br>apmo</p></div>
<svg class="abs" style="left:914px;top:3080px" width="24" height="28" viewBox="0 0 24 28"><rect x="1" y="1" width="22" height="26" fill="none" stroke="#a3e300" stroke-width="2"/><path d="M8 8v10l4 4h6v-8l-6-2v-4z" fill="#a3e300"/></svg>
<span class="vline" style="left:996px;top:3072px"></span>
<div class="cta-feature" style="left:1011px;top:3071px"><h5>Easy<br>payments</h5><p>Lorem ipsum</p></div>

<footer class="footer">
  <div class="brand" style="left:71px;top:52px;font-size:18px"><span class="brand-mark" style="width:22px;height:22px"></span>Dr. Wanbrook Consult</div>
  <p class="footer-about">Lorem ipsum dolor sit amet, consy ect etu o dolor sitct raqum nemo de amet.</p>
  <span class="social" style="left:65px"></span>
  <span class="social" style="left:123px"></span>
  <span class="social" style="left:180px"></span>
  <span class="social" style="left:239px"></span>
  <h6 style="left:440px">Contact info</h6>
  <ul class="contact">
    <li>48 Harrowgate Lane, Suite 12, London</li>
    <li>London, United Kingdom</li>
    <li>hello@wanbrook.example</li>
    <li>+44 (0) 555 0100 200</li>
  </ul>
  <h6 style="left:816px">Useful resources</h6>
  <ul class="resources">
    <li>Home</li><li>Team</li><li>Lean Construction</li><li>Lean Equipment</li><li>Lean Design</li><li>Lean Training</li>
  </ul>
</footer>
<div class="copyright">© 2020 Dr.Wanbrook Consult</div>

</body>
</html>
```